Renata Quisby

Luxury And Style -

Black - White & Gold

Target Market(s)

Fashion

Industry/Entity Type

Fashion

Requirements
Must have
• High-End
Nice to have
• We will Print on Silk Paper

```html
<!DOCTYPE html>
<html lang="en">
<head>
<meta charset="UTF-8">
<title>Renata Quisby Letterhead</title>
<link href="https://fonts.googleapis.com/css2?family=Source+Sans+3:wght@400;600&display=swap" rel="stylesheet">
<style>
  :root {
    --backdrop: #e4e4e4;
    --paper: #ffffff;
    --gold: #a9823a;
    --gold-light: #c9a55a;
    --black: #1c1c1c;
    --ink: #333333;
  }
  * { margin: 0; padding: 0; box-sizing: border-box; }
  html, body { width: 1200px; height: 960px; overflow: hidden; background: var(--backdrop); }
  body { font-family: "Source Sans 3", sans-serif; color: var(--ink); }
  .letterhead {
    position: absolute; left: 275px; top: 20px;
    width: 650px; height: 920px;
    background: var(--paper);
    overflow: hidden;
    box-shadow: 0 6px 24px rgba(0,0,0,0.12);
  }
  .brand { position: absolute; left: 56px; top: 62px; display: flex; align-items: center; gap: 10px; }
  .brand-mark { width: 14px; height: 14px; border-radius: 50%; background: var(--gold); }
  .brand-name { font-size: 24px; font-weight: 400; color: var(--black); letter-spacing: 3px; text-transform: uppercase; }
  .brand-tagline { position: absolute; left: 80px; top: 96px; font-size: 10px; color: var(--gold); letter-spacing: 1px; text-transform: uppercase; }
  .contact {
    position: absolute; right: 56px; top: 50px;
    border-left: 1.5px solid var(--gold); padding-left: 14px;
    font-size: 11.5px; line-height: 1.45; font-style: normal;
  }
  .contact-row { display: flex; align-items: center; gap: 6px; }
  .contact-row svg { width: 10px; height: 10px; fill: var(--gold); }
  .recipient { position: absolute; left: 56px; top: 170px; font-size: 11.5px; line-height: 1.4; }
  .recipient-name { font-size: 14px; text-transform: uppercase; color: var(--black); }
  .body-copy { position: absolute; left: 56px; top: 245px; width: 520px; font-size: 11px; line-height: 1.55; }
  .body-copy p { margin-bottom: 14px; }
  .closing { position: absolute; left: 56px; top: 600px; font-size: 11.5px; }
  .closing-name { margin-top: 30px; font-size: 15px; color: var(--black); }
  .footer-band { position: absolute; left: 0; bottom: 0; width: 650px; height: 340px; }
  .footer-name {
    position: absolute; right: 34px; bottom: 150px;
    font-size: 22px; font-weight: 400; letter-spacing: 3px; text-transform: uppercase;
    color: var(--paper);
  }
</style>
</head>
<body>
  <main class="letterhead">
    <div class="brand">
      <span class="brand-mark"></span>
      <span class="brand-name">Renata Quisby</span>
    </div>
    <div class="brand-tagline">Luxury and Style</div>

    <address class="contact">
      <div>Your address, City</div>
      <div>State, Zip 1234</div>
      <div class="contact-row"><svg viewBox="0 0 10 10"><path d="M2 1h2l1 2-1.2 1a5 5 0 0 0 2.2 2.2L7 5l2 1v2a1 1 0 0 1-1 1A8 8 0 0 1 1 2a1 1 0 0 1 1-1z"/></svg>123 456 789</div>
      <div class="contact-row"><svg viewBox="0 0 10 10"><path d="M0 2h10v6H0z M0 2l5 3.5L10 2" stroke="#fff" stroke-width="0.8"/></svg>info@yourgmail.com</div>
      <div class="contact-row"><svg viewBox="0 0 10 10"><circle cx="5" cy="5" r="4.5"/></svg>www.yourwebsite.com</div>
    </address>

    <section class="recipient">
      <div class="recipient-name">Dorian Felsby</div>
      <div>Chief Exective Officer</div>
      <div>City/State, Zip Code</div>
    </section>

    <section class="body-copy">
      <p>Proin gravida nibh vel velit auctor aliquet. Aenean sollicitudin, lorem quis bibendum auctor, nisi elit consequat ipsum, nec sagittis sem nibh id elit. Duis sed odio sit amet nibh vulputate cursus a sit amet mauris. Morbi accumsan ipsum velit. Nam nec tellus a odio tincidunt auctor a ornare odio. Sed non mauris vitae erat consequat auctor eu in elit. Class aptent taciti sociosqu ad litora torquent ugue. Sed non neque elit. Sed ut imperdiet nisi. Proin condimentum fermentum nunc. Etiam pharetra, imperdiet nisi. Proin condimentum fermentum nunc. Etiam pharetra, erat sed fermentum feugiat, velit mauris egestas quam, ut aliquam massa nisl quis neque. Suspendisse in orci enim.</p>
      <p>This is Photoshop's version of Lorem Ipsum. Proin gravida nibh vel velit auctor aliquet. Aenean sollicitudin, lorem quis bibendum auctor, nisi elit consequat ipsum, nec sagittis sem nibh id elit. Duis sed odio sit amet nibh vulputate cursus a sit amet mauris. Mo rbi accumsan ipsum velit. Nam nec tellus a odio tincidunt auctor a ornare odio. Sed non mauris vitae erat consequat auctor eu in elit. Class aptt taciti sociosqu ad litora torquent per conubia nostra, per inceptos himenaeos. Mauris in erat justo.</p>
      <p>Nullam ac urna eu felis dapibus condimentum sit amet a augue. Sed non neque elit. Sed ut imperdiet nisi. Proin condimentum fermentum nunc. Etiam pharetra, erat sed fermentum feugiat, velit mauris egestas quam. Nullam ac urna eu felis dapibus condimentum sit amet a aug pharetra, erat sed fermentum feugiat, velit mauris egestas quam. Nullam ac urna eu felis dapibus condimentum sit amet a augue. Sed non neque elit. Sed ut imperdiet nisi. Proin condimentum fermentum nunc.</p>
    </section>

    <section class="closing">
      <div>Sincerely,</div>
      <div class="closing-name">Arlo Penwright</div>
    </section>

    <svg class="footer-band" viewBox="0 0 650 340" preserveAspectRatio="none" aria-hidden="true">
      <path d="M0 340 L0 318 C240 280 420 200 520 60 C560 20 610 8 650 0 L650 340 Z" fill="var(--gold)"/>
      <path d="M0 322 C230 290 400 215 500 90" fill="none" stroke="var(--paper)" stroke-width="4"/>
      <path d="M0 312 C220 282 390 210 480 120 C410 230 220 300 0 326 Z" fill="var(--black)"/>
    </svg>
    <div class="footer-name">Renata Quisby</div>
  </main>
</body>
</html>
```